Business Card Design Project

for a second hand vintage clothing store. shop name is The Velvet Loft

Cards to be double sided

The name on the card is Marianne Trelford

Information to put on card:

The Velvet Loft
Marianne Trelford (no job title)
84/227 Quayle St, Pyrmont, Sydney, NSW, 2009.
Mobile: 0412 975 206
Email: thevelvetloft@mailbox-example.com.au
Web: www.thevelvetloft-example.com.au

Target Market(s)

Women looking at vintage clothing

Industry/Entity Type

Clothing

```html
<!DOCTYPE html>
<html lang="en">
<head>
<meta charset="utf-8">
<title>The Velvet Loft — Business Card</title>
<link rel="stylesheet" href="https://fonts.googleapis.com/css2?family=Libre+Franklin:wght@400;600&display=swap">
<style>
  :root {
    --backdrop: #e4e2de;
    --wine: #5a2233;
    --cream: #ead890;
    --cream-text: #f0dc98;
    --brush-tan: #d2b57c;
    --shadow: rgba(0, 0, 0, 0.28);
  }
  * { box-sizing: border-box; margin: 0; padding: 0; }
  html, body {
    width: 1200px;
    height: 875px;
    overflow: hidden;
    background: var(--backdrop);
    font-family: "Libre Franklin", Arial, sans-serif;
  }
  .canvas {
    position: relative;
    width: 1200px;
    height: 875px;
  }
  .card {
    position: absolute;
    width: 580px;
    height: 355px;
    border-radius: 30px;
    box-shadow: 6px 10px 22px var(--shadow);
    overflow: hidden;
  }
  .card--front {
    left: 140px;
    top: 45px;
    background: var(--wine);
    color: var(--cream-text);
  }
  .card--back {
    left: 480px;
    top: 455px;
    background: var(--cream);
    color: var(--wine);
  }
  .wordmark {
    position: absolute;
    font-weight: 400;
    font-size: 42px;
    letter-spacing: 0.5px;
    white-space: nowrap;
  }
  .card--front .wordmark { left: 40px; top: 80px; color: var(--cream-text); }
  .card--back .wordmark { left: 120px; top: 140px; font-size: 46px; color: var(--wine); }

  .sign-off {
    position: absolute;
    right: 24px;
    bottom: 20px;
    display: flex;
    align-items: flex-end;
    gap: 8px;
  }
  .holder {
    font-weight: 600;
    font-size: 16px;
    line-height: 19px;
    letter-spacing: 0.4px;
    white-space: nowrap;
  }
  .contact {
    padding-left: 8px;
    border-left: 1.5px solid var(--cream-text);
    font-size: 12.5px;
    line-height: 19px;
    list-style: none;
    white-space: nowrap;
  }
  .brush-area {
    position: absolute;
    left: 45px;
    top: 30px;
    width: 110px;
    height: 310px;
    border-radius: 40% 55% 45% 50%;
    background: linear-gradient(180deg, rgba(210,181,124,0.55), var(--brush-tan) 45%, rgba(210,181,124,0.7));
  }
  .address {
    position: absolute;
    right: 34px;
    bottom: 48px;
    font-size: 14px;
    line-height: 19px;
    font-style: normal;
    letter-spacing: 0.3px;
  }
</style>
</head>
<body>
<main class="canvas">
  <section class="card card--front" aria-label="Card front">
    <div class="wordmark">The Velvet Loft</div>
    <div class="sign-off">
      <p class="holder">Marianne Trelford</p>
      <ul class="contact">
        <li>M: 0412 975 206</li>
        <li>E: thevelvetloft@mailbox-example.com.au</li>
        <li>W: www.thevelvetloft-example.com.au</li>
      </ul>
    </div>
  </section>

  <section class="card card--back" aria-label="Card back">
    <div class="brush-area" role="img" aria-label="Loose tan brush-stroke texture"></div>
    <div class="wordmark">The Velvet Loft</div>
    <address class="address">84/227 Quayle St, Pyrmont,<br>Sydney, NSW, 2009.</address>
  </section>
</main>
</body>
</html>
```